Shine4all

Full service cleaning company. Specializing in commercial and apartment cleans.
Fully licensed and insured
Digital photos and invoices provided
for every job
For web designer...basic info as expected by a highend cleaning company that provides excellent service at reasonable pricing. We are going after large property management companies as well as not pricing ourselves out to help the local mom and pop companies as well.
Updates

Project Deadline Extended Reason: Everyone seems to be having trouble understanding that we are a dumpster company that is adding a cleaning side to the company. We want our clients to see Shine4All as a separate branch of our our already established waste management company.We are not a regular cleaning company. We specialize in going after large commercial cleans and apartment cleans. I have now included info regarding a proposal for work and our invoice/job completion to make it clearer what we do Added Monday, July 20, 2015

Target Market(s)

Property Management companies in Savannah, Richmond Hill, Rincon, Hinesville and Midway Georgia

Industry/Entity Type

Cleaning Service

Coding

Coded - Design and coding required

Number of Pages Required

3 page

Requirements
Must have
• Nice home page with lots of photos (stock are fine) to convey exactly what we do (getting logo bid on right now on this sight).
• Information page with employee photos (can leave blank) need room for 4 photos and bios.
• Page or link to a static page for the dumpster company BinTrek (logo for this is red and black file attached along with photo of dumpster. This page just needs to be one page with contact info and information about commercial dumpster.
• Basically this site is just a fluff page used for marketing purposes. Its content can be general and once created wont change much. Services and photos can be provided upon request but general layout and info is what we are looking for.

```html
<!DOCTYPE html>
<html lang="en">
<head>
<meta charset="utf-8">
<title>Shine4All – Commercial &amp; Apartment Cleaning</title>
<link rel="stylesheet" href="https://fonts.googleapis.com/css2?family=Open+Sans:wght@400;600;700&family=Raleway:wght@400;500;600&display=swap">
<style>
:root{
  --red:#e21b1b;
  --red-dark:#b51212;
  --ink:#333333;
  --muted:#666666;
  --light:#f4f4f4;
  --line:#dddddd;
  --footer:#2b2b2b;
  --footer-text:#bbbbbb;
  --white:#ffffff;
}
*{box-sizing:border-box;margin:0;padding:0}
html,body{width:791px;height:1200px;overflow:hidden}
body{font-family:"Open Sans",Arial,sans-serif;color:var(--ink);background:var(--white);font-size:10px;line-height:1.5}
.site-header{height:92px;display:flex;justify-content:space-between;align-items:center;padding:0 48px 0 88px}
.brand{display:flex;align-items:center;gap:10px}
.brand-mark{width:30px;height:30px;background:var(--red)}
.brand-name{font-family:"Raleway",sans-serif;font-weight:600;font-size:30px;color:var(--ink);letter-spacing:.5px}
.header-right{text-align:right}
.social{display:flex;gap:6px;justify-content:flex-end;margin-bottom:8px}
.social span{width:20px;height:20px;border-radius:50%;background:var(--red);display:block}
.tollfree{font-size:11px;color:var(--muted);display:flex;align-items:center;gap:5px;justify-content:flex-end}
.tollfree b{color:var(--red);font-weight:600}
.main-nav{height:32px;background:var(--red);display:flex;justify-content:center;padding-left:20px}
.main-nav a{color:var(--white);text-decoration:none;font-size:10px;font-weight:600;text-transform:uppercase;padding:0 26px;line-height:32px}
.main-nav a.active{background:#222}
.hero{position:relative;height:272px;background:linear-gradient(180deg,#dadada 0%,#bdbdbd 55%,#9a9a9a 100%)}
.hero-caption{position:absolute;left:0;right:0;bottom:14px;background:rgba(40,40,40,.82);color:var(--white);text-align:center;font-family:"Raleway",sans-serif;font-size:17px;line-height:26px;padding:6px 0}
.audience{display:flex;justify-content:center;gap:60px;padding:32px 0 24px;border-bottom:1px solid var(--line)}
.audience a{width:192px;height:60px;background:var(--red);border-radius:3px;display:flex;align-items:center;gap:10px;padding-left:16px;color:var(--white);text-decoration:none;font-family:"Raleway",sans-serif;font-size:14px;white-space:nowrap}
.audience .icon{width:34px;height:34px;border-radius:50%;background:var(--white);display:flex;align-items:center;justify-content:center;flex:none}
.welcome{display:flex;gap:30px;padding:22px 88px 0;height:180px}
.welcome-text{flex:1}
.welcome h2{font-size:17px;font-weight:600;margin-bottom:6px}
.welcome p{font-size:10px;color:var(--muted);line-height:1.6}
.more{color:var(--red);font-weight:600;text-decoration:none;font-size:10px}
.video{width:180px;height:128px;background:linear-gradient(160deg,#7ea5c4,#4f7a3a 70%,#6e6e6e);position:relative;margin-top:4px}
.video .play{position:absolute;left:70px;top:42px}
.video .bar{position:absolute;left:0;right:0;bottom:0;height:14px;background:rgba(0,0,0,.7)}
.cta{height:132px;background:linear-gradient(180deg,#4b4b4b,#2f2f2f);text-align:center;color:var(--white);padding-top:22px}
.cta h3{font-family:"Raleway",sans-serif;font-weight:400;font-size:21px;line-height:26px}
.cta form{display:flex;justify-content:center;margin-top:12px}
.cta input{width:160px;height:22px;border:0;padding:0 8px;font-size:9px;font-family:inherit}
.cta button{height:22px;background:var(--red);color:var(--white);border:0;font-size:9px;font-weight:700;padding:0 12px;font-family:inherit;margin-left:4px}
.lower{display:flex;gap:40px;padding:20px 88px 0;height:205px}
.lower h2{font-family:"Raleway",sans-serif;font-size:16px;font-weight:500;margin-bottom:12px}
.lower h2 em{font-style:normal;color:var(--red)}
.testimonials{flex:1.35}
.quote{display:flex;gap:14px}
.avatar{width:62px;height:62px;border-radius:50%;background:linear-gradient(135deg,#e8c9b5,#b97c62);flex:none;border:3px solid var(--light)}
.quote p{color:var(--muted);font-size:10px}
.quote cite{display:block;color:var(--red);font-style:normal;font-size:9px;margin-top:4px}
.quote .more{display:block;text-align:right;color:var(--ink);font-size:9px}
.why{flex:1}
.why-head{display:flex;justify-content:space-between;align-items:baseline}
.why-head span{color:#999;font-size:12px}
.why ul{list-style:none}
.why li{font-size:9px;color:var(--muted);border-bottom:1px solid var(--line);padding:3px 0;display:flex;gap:6px;align-items:center}
.site-footer{background:var(--footer);height:145px;display:flex;gap:30px;padding:14px 60px 0 88px;color:var(--footer-text);font-size:9px}
.site-footer h4{color:var(--white);font-size:11px;font-weight:400;margin-bottom:5px}
.site-footer ul{list-style:none;line-height:1.6}
.col-links{width:90px}
.col-contact{width:140px}
.col-faq{width:150px}
.col-connect{flex:1;text-align:right}
.col-connect .social{margin-bottom:8px}
.truck-art{width:90px;height:56px;background:linear-gradient(180deg,#555,#444);margin-left:auto;border-radius:4px}
.copyright{height:25px;background:var(--red);color:var(--white);font-size:9px;text-align:center;line-height:25px}
</style>
</head>
<body>
<header class="site-header">
  <div class="brand"><span class="brand-mark"></span><span class="brand-name">SHINE4ALL</span></div>
  <div class="header-right">
    <div class="social"><span></span><span></span><span></span></div>
    <div class="tollfree">
      <svg width="12" height="12" viewBox="0 0 24 24"><circle cx="12" cy="12" r="12" fill="#e21b1b"/><path d="M8 6l2 0 1 3-1.5 1a7 7 0 0 0 4.5 4.5l1-1.5 3 1 0 2c0 1-1 2-2 2A11 11 0 0 1 6 8c0-1 1-2 2-2z" fill="#fff"/></svg>
      Toll Free <b>800 555 0142</b>
    </div>
  </div>
</header>

<nav class="main-nav">
  <a class="active" href="#">Home</a><a href="#">About Us</a><a href="#">Services</a><a href="#">Think Green</a><a href="#">Customer Reviews</a><a href="#">Contact Us</a>
</nav>

<section class="hero" role="img" aria-label="Black and white photo of a city skyline with commercial and apartment buildings">
  <div class="hero-caption">We Are A Full Service Cleaning Company Specializing In Commercial<br>And Apartment Cleans</div>
</section>

<section class="audience">
  <a href="#"><span class="icon"><svg width="18" height="18" viewBox="0 0 24 24"><path d="M3 12l9-8 9 8h-3v8h-4v-5h-4v5H6v-8z" fill="#e21b1b"/></svg></span>Home Owner</a>
  <a href="#"><span class="icon"><svg width="18" height="18" viewBox="0 0 24 24"><path d="M4 8h16v11H4zM9 8V5h6v3" fill="none" stroke="#e21b1b" stroke-width="2.5"/></svg></span>Business Owner</a>
  <a href="#"><span class="icon"><svg width="18" height="18" viewBox="0 0 24 24"><path d="M3 9h18l-2 10H5z" fill="#e21b1b"/><rect x="2" y="6" width="20" height="3" fill="#e21b1b"/></svg></span>Rent-a-Dumpster</a>
</section>

<section class="welcome">
  <div class="welcome-text">
    <h2>Welcome to Shine4All</h2>
    <p>We clean large commercial buildings and apartment units across coastal Georgia. Our crews are fully licensed and insured, and every job comes with digital photos and a clear invoice. Property managers trust us for fast turnovers, fair pricing and steady service, while local family businesses get the same care at a rate that fits.</p>
    <a class="more" href="#">Read More &gt;&gt;</a>
  </div>
  <div class="video" role="img" aria-label="Video still of a roll-off dumpster truck on a job site">
    <svg class="play" width="40" height="40" viewBox="0 0 40 40"><circle cx="20" cy="20" r="20" fill="rgba(255,255,255,.85)"/><path d="M16 12l12 8-12 8z" fill="#333"/></svg>
    <div class="bar"></div>
  </div>
</section>

<section class="cta" role="img" aria-label="Dark photo of a dumpster at a work site behind the call to action">
  <h3>Ready to get started? See what dumpsters are<br>available in your area.</h3>
  <form><input type="text" placeholder="Enter ZIP or Postal Code"><button type="button">SHOW PRODUCTS</button></form>
</section>

<section class="lower">
  <div class="testimonials">
    <h2>What Client <em>Say About Us</em></h2>
    <div class="quote">
      <div class="avatar" role="img" aria-label="Portrait photo of the client"></div>
      <div>
        <p>Their crew turned over twelve apartment units in two days and sent photos of every room. The invoice was clear, the price was fair and our tenants moved in on time. We now book them for every cleanout.</p>
        <cite>— Dana Whitfield, Pooler Property Group</cite>
        <a class="more" href="#">Read More Testimonials »</a>
      </div>
    </div>
  </div>
  <div class="why">
    <div class="why-head"><h2>Why <em>Choose Us</em></h2><span>‹ ›</span></div>
    <ul>
      <li><svg width="9" height="9" viewBox="0 0 10 10"><path d="M1 5l3 3 5-6" stroke="#e21b1b" stroke-width="2" fill="none"/></svg>Wide selection of dumpster sizes available</li>
      <li><svg width="9" height="9" viewBox="0 0 10 10"><path d="M1 5l3 3 5-6" stroke="#e21b1b" stroke-width="2" fill="none"/></svg>Flexible, timely pickup and delivery</li>
      <li><svg width="9" height="9" viewBox="0 0 10 10"><path d="M1 5l3 3 5-6" stroke="#e21b1b" stroke-width="2" fill="none"/></svg>Rush service available</li>
      <li><svg width="9" height="9" viewBox="0 0 10 10"><path d="M1 5l3 3 5-6" stroke="#e21b1b" stroke-width="2" fill="none"/></svg>Easy online ordering and scheduling</li>
      <li><svg width="9" height="9" viewBox="0 0 10 10"><path d="M1 5l3 3 5-6" stroke="#e21b1b" stroke-width="2" fill="none"/></svg>Online account management</li>
      <li><svg width="9" height="9" viewBox="0 0 10 10"><path d="M1 5l3 3 5-6" stroke="#e21b1b" stroke-width="2" fill="none"/></svg>Secure online payment</li>
    </ul>
  </div>
</section>

<footer class="site-footer">
  <div class="col-links"><h4>Quick Links</h4><ul><li>Home</li><li>About Us</li><li>Services</li><li>Think Green</li><li>Customer Reviews</li><li>Contact Us</li></ul></div>
  <div class="col-contact"><h4>Contact Details</h4><ul><li><b style="color:#fff;font-weight:600">Shine4All</b></li><li>1250 Harbor Street,<br>Savannah, GA 31401</li><li>800 555 0142</li><li>hello@shine4all.com</li></ul></div>
  <div class="col-faq"><h4>FAQ's</h4><ul><li>What sizes of dumpsters do we offer?</li><li>How much does a dumpster cost?</li><li>How long can we keep the dumpster?</li><li>More FAQs »</li></ul></div>
  <div class="col-connect"><h4>Connect With Us</h4><div class="social"><span></span><span></span><span></span><span></span></div><div class="truck-art" role="img" aria-label="Grey illustration of a roll-off dumpster truck"></div></div>
</footer>
<div class="copyright">Copyright © 2015 Shine4All | All Rights Reserved</div>
</body>
</html>
```